Dental Specialist Needs a Business Card

We are a state of the art dental specialty office and need a business card that looks modern but professional.
I have provided our logo design in both vertical and horizontal. We use the design on letterhead in the vertical format but provided both forms for you. Thanks
Updates

Please add the address, phone and fax numbers I listed to all designs and please leave a space for website and for my employee name on each design. Thanks 2847 Marlow Avenue, Suite K East Brantham, NY 14391 Phone (716)392-5174 Fax:(716)392-5179 My name is Devin R.Holloway,D.D.S. If you want to show it with my name but the design needs to allow for the name to be switched.

Industry/Entity Type

Business

```html
<!DOCTYPE html>
<html lang="en">
<head>
<meta charset="utf-8">
<title>Keystone Endodontics – Business Card</title>
<link href="https://fonts.googleapis.com/css2?family=Bitter:wght@400;600&display=swap" rel="stylesheet">
<style>
  :root{
    --backdrop:#1b1b1b;
    --card-white:#fbfbfa;
    --ink:#161616;
    --green:#52c08a;
    --teal:#2fb7a6;
    --blue:#1ea7cc;
    --icon:#2bb0a8;
    --on-panel:#ffffff;
    --rule:rgba(255,255,255,.7);
  }
  *{margin:0;padding:0;box-sizing:border-box}
  html,body{width:1200px;height:1000px;overflow:hidden;background:var(--backdrop)}
  body{font-family:"Bitter",Georgia,serif;position:relative}

  .business-card{
    position:absolute;left:100px;top:215px;width:1000px;height:570px;
    background:var(--card-white);overflow:hidden;border-radius:4px;
  }

  /* brand side */
  .brand-side{position:absolute;left:0;top:0;width:460px;height:100%;
    display:flex;align-items:center;justify-content:center;gap:16px}
  .brand-dot{width:26px;height:26px;border-radius:50%;background:var(--icon);flex:none}
  .brand-name{font-weight:600;font-size:34px;line-height:1.15;color:var(--ink)}

  /* contact side */
  .contact-side{
    position:absolute;left:460px;top:0;right:0;bottom:0;
    background:linear-gradient(160deg,var(--green) 0%,var(--teal) 50%,var(--blue) 100%);
    color:var(--on-panel);
  }
  .contact-side .art-field{
    position:absolute;inset:0;
    background:radial-gradient(ellipse at 35% 45%,rgba(255,255,255,.18),rgba(255,255,255,0) 60%);
  }
  .holder{position:absolute;left:80px;top:42px;right:50px}
  .holder-name{font-size:40px;font-weight:400;letter-spacing:.3px}
  .holder-title{font-size:22px;margin-top:2px}
  .holder-rule{height:1px;background:var(--rule);margin-top:22px;width:100%}

  .contact-row{position:absolute;left:0;display:flex;align-items:center;height:44px}
  .contact-tab{
    width:48px;height:44px;background:var(--card-white);
    border-radius:0 22px 22px 0;display:flex;align-items:center;justify-content:center;
  }
  .contact-tab svg{width:20px;height:20px;fill:var(--icon)}
  .contact-text{margin-left:34px;font-size:22px;line-height:1.2}
  .row-address{top:214px}
  .row-address .contact-text{margin-top:-6px}
  .row-phone{top:284px}
  .row-fax{top:354px}
  .row-web{top:424px}
</style>
</head>
<body>
  <div class="business-card">
    <section class="brand-side">
      <span class="brand-dot"></span>
      <div class="brand-name">Keystone<br>Endodontics P.C.</div>
    </section>

    <section class="contact-side">
      <div class="art-field" role="img" aria-label="Soft faint decorative swirl in light tones"></div>

      <div class="holder">
        <div class="holder-name">Devin R. Holloway</div>
        <div class="holder-title">Doctor of Dental Surgery</div>
        <div class="holder-rule"></div>
      </div>

      <div class="contact-row row-address">
        <span class="contact-tab"><svg viewBox="0 0 24 24"><path d="M12 2a7 7 0 0 0-7 7c0 5.2 7 13 7 13s7-7.8 7-13a7 7 0 0 0-7-7zm0 9.5A2.5 2.5 0 1 1 12 6.5a2.5 2.5 0 0 1 0 5z"/></svg></span>
        <span class="contact-text">2847 Marlow Avenue, Suite K<br>East Brantham, NY 14391</span>
      </div>

      <div class="contact-row row-phone">
        <span class="contact-tab"><svg viewBox="0 0 24 24"><path d="M6.6 10.8a15.1 15.1 0 0 0 6.6 6.6l2.2-2.2a1 1 0 0 1 1-.25 11.4 11.4 0 0 0 3.6.57 1 1 0 0 1 1 1V20a1 1 0 0 1-1 1A17 17 0 0 1 3 4a1 1 0 0 1 1-1h3.5a1 1 0 0 1 1 1c0 1.25.2 2.45.57 3.57a1 1 0 0 1-.25 1z"/></svg></span>
        <span class="contact-text">(716) 392-5174</span>
      </div>

      <div class="contact-row row-fax">
        <span class="contact-tab"><svg viewBox="0 0 24 24"><path d="M7 3h8l3 3v4H7zM4 11h16a2 2 0 0 1 2 2v6a2 2 0 0 1-2 2H4a2 2 0 0 1-2-2v-6a2 2 0 0 1 2-2zm3 3v2h4v-2zm7 0v2h2v-2z"/></svg></span>
        <span class="contact-text">(716) 392-5179</span>
      </div>

      <div class="contact-row row-web">
        <span class="contact-tab"><svg viewBox="0 0 24 24"><path d="M12 2a10 10 0 1 0 0 20 10 10 0 0 0 0-20zm6.9 6h-2.9a15.6 15.6 0 0 0-1.4-3.6A8 8 0 0 1 18.9 8zM12 4c.8 1.2 1.5 2.5 1.9 4h-3.8c.4-1.5 1.1-2.8 1.9-4zM4.3 14a8 8 0 0 1 0-4h3.4a16 16 0 0 0 0 4zm.8 2h2.9c.3 1.3.8 2.5 1.4 3.6A8 8 0 0 1 5.1 16zM8 8H5.1a8 8 0 0 1 4.3-3.6C8.8 5.5 8.3 6.7 8 8zm4 12c-.8-1.2-1.5-2.5-1.9-4h3.8c-.4 1.5-1.1 2.8-1.9 4zm2.3-6H9.7a14 14 0 0 1 0-4h4.6a14 14 0 0 1 0 4zm.3 5.6c.6-1.1 1.1-2.3 1.4-3.6h2.9a8 8 0 0 1-4.3 3.6zm1.7-5.6a16 16 0 0 0 0-4h3.4a8 8 0 0 1 0 4z"/></svg></span>
        <span class="contact-text">www.keystoneendo.com</span>
      </div>
    </section>
  </div>
</body>
</html>
```